Flyer für eine Imkerei
Wunderbare unkomplizierte Zusammenarbeit mit einem tollen Designer. Extrem gutes Verständnis der Grundidee, super flexibles einarbeiten eigener Verbesserungsvorschläge - einfach sehr kompetent! Danke dafür.
Zielgruppe
Ich bin Hobbyimker mit einer sehr kleinen Imkerei im Dorf. Ich biete lokalen Honig an. Der Flyer soll ein Infoflyer für Kunden und evt. Neukunden sein.
Aufgabenstellung
Bitte im Wickelfalz hochkant A4, (gefaltet also 99x210). Textbausteine sind als Datei angehängt. Bitte nur den Text nutzen, nicht Schriftgröße, Schritart etc. Ebenso ist eigenes Bildmaterial vorhanden. Ich würde mich über ein edles aber schlicht modernes Design freuen. Das Design darf gern Honigwaben (Hexagon) als Grundidee beinhalten. Bevorzugte Farbtöne sind schwarz, gold, gelb, orange (honigfarben) bis Weinrot (siehe Honigetikett auf dem Foto).

```html
<!DOCTYPE html>
<html lang="de">
<head>
<meta charset="utf-8">
<title>Imkerei Saaletal – Flyer</title>
<link rel="stylesheet" href="https://fonts.googleapis.com/css2?family=Montserrat:wght@600;700;800&family=Roboto:wght@400;500;700&display=swap">
<style>
:root{
  --bg:#a7a7a9;
  --black:#0b0b0b;
  --white:#ffffff;
  --paper:#f7f7f7;
  --orange:#f29400;
  --orange-deep:#e07b00;
  --gold:#f7b21d;
  --yellow:#ffd43a;
  --wine:#a8321a;
  --text:#1f1f1f;
}
*{margin:0;padding:0;box-sizing:border-box}
html,body{width:1200px;height:2317px;overflow:hidden;background:var(--bg)}
body{font-family:"Roboto",Arial,sans-serif;color:var(--text);position:relative}
.sheet{position:absolute;left:60px;width:1080px;height:763px;box-shadow:0 4px 14px rgba(0,0,0,.25);overflow:hidden}
.sheet.outside{top:375px}
.sheet.inside{top:1178px}
.spread{position:absolute;left:0;top:0;width:800px;height:565px;transform:scale(1.35);transform-origin:0 0;overflow:hidden}
.abs{position:absolute}
.fill{position:absolute}
.heading{font-family:"Montserrat",Arial,sans-serif;font-weight:700;color:var(--orange)}
.center{text-align:center}

/* outside */
.about{left:0;top:0;width:267px;height:565px;background:var(--white)}
.about-title{left:0;width:267px;top:28px;font-size:13px}
.about-text{left:20px;width:227px;top:56px;font-size:8.6px;line-height:13.2px;font-weight:700;color:var(--black)}
.about-text p+p{margin-top:13px}
.honeycomb-band{left:0;top:200px;width:267px;height:70px;background:linear-gradient(90deg,var(--gold),var(--orange) 35%,var(--yellow) 55%,var(--orange-deep) 80%,var(--gold))}
.bottles-photo{left:0;top:255px;width:267px;height:150px;background:linear-gradient(180deg,#6b3a08 0%,#b4600c 40%,#7a3306 75%,var(--black) 100%)}
.about-dark{left:0;top:400px;width:267px;height:165px;background:var(--black)}
.nature-title{left:0;width:267px;top:400px;font-size:12.5px;color:var(--gold)}
.nature-text{left:18px;width:231px;top:427px;font-size:8.3px;line-height:12.6px;font-weight:700;color:var(--white)}

.contact{left:267px;top:0;width:266px;height:565px;background:var(--black)}
.hive-photo{left:0;top:0;width:266px;height:440px;background:linear-gradient(180deg,#2c5ca8 0%,#6c98c9 18%,#4e7a2c 42%,#8f6a32 60%,#3f5e20 85%,#1a2410 100%)}
.try-box{left:21px;top:303px;width:224px;height:100px;border-radius:6px;background:linear-gradient(180deg,var(--gold),var(--orange-deep));padding:8px 8px 0}
.try-title{font-family:"Montserrat",Arial,sans-serif;font-weight:700;font-size:14.5px;color:var(--black)}
.try-text{margin-top:7px;font-size:8.2px;line-height:12.2px;color:var(--black)}
.try-text b{font-weight:700}
.address{left:0;width:266px;top:425px;font-size:8.2px;color:var(--white)}
.order{left:0;width:266px;top:445px;font-size:10.5px;line-height:13px;font-weight:700;color:var(--orange)}
.phone{left:0;width:266px;top:476px;font-family:"Montserrat",Arial,sans-serif;font-weight:800;font-size:18px;letter-spacing:.5px;color:var(--orange)}
.welcome{left:0;width:266px;top:514px;font-size:8.2px;color:var(--white)}

.cover{left:533px;top:0;width:267px;height:565px;background:var(--white)}
.cover-title{left:0;width:267px;top:26px;font-size:16.5px;line-height:19px;font-weight:800;color:var(--orange)}
.cover-sub{left:0;width:267px;top:68px;font-size:10.2px;color:var(--black)}
.cover-photo{left:0;top:98px;width:267px;height:467px;background:linear-gradient(180deg,var(--orange) 0%,var(--yellow) 18%,#f4c51a 35%,#b35b0a 55%,#5a2a08 78%,#120c05 100%)}
.family{left:0;width:267px;top:500px;font-size:8.2px;line-height:11px;color:var(--white)}

/* inside */
.inside-bg{left:0;top:0;width:800px;height:565px}
.photo-herb{left:0;top:0;width:267px;height:200px;background:linear-gradient(180deg,#2a3a1c,#6b5a7c 45%,#2e4a1e)}
.photo-bees{left:267px;top:0;width:266px;height:200px;background:linear-gradient(180deg,#d9c4a0,#8a6a3e 55%,#3a2a18)}
.photo-flower{left:533px;top:0;width:267px;height:200px;background:linear-gradient(180deg,#3d4a2a,#f2d21e 45%,#2f5a1e)}
.band-label{font-family:"Montserrat",Arial,sans-serif;font-weight:800;color:var(--white);font-size:11px;letter-spacing:.4px;white-space:nowrap}
.label-honey{left:72px;top:94px;transform:rotate(2deg)}
.label-regional{left:385px;top:128px;transform:rotate(14deg)}
.label-world{left:582px;top:178px;transform:rotate(-9deg)}

.intro{left:30px;top:222px;width:210px;font-size:7.3px;line-height:12.2px;font-weight:700;color:var(--orange)}
.pill{left:33px;width:200px;height:18px;border-radius:9px;background:linear-gradient(180deg,var(--gold),var(--orange-deep));font-size:7.4px;font-weight:700;color:var(--black);text-align:center;line-height:18px;box-shadow:0 1px 2px rgba(0,0,0,.3)}
.sort-text{left:30px;width:210px;font-size:7.2px;line-height:11.3px;color:var(--text)}
.note-box{left:30px;top:466px;width:210px;height:70px;border-radius:5px;background:linear-gradient(180deg,var(--gold),var(--orange-deep));font-size:7.2px;line-height:10.8px;color:var(--black);text-align:center;padding:7px 6px 0;box-shadow:0 1px 2px rgba(0,0,0,.3)}

.regional-title{left:285px;top:220px;font-size:12.5px;line-height:14px}
.reason{left:290px;width:225px}
.reason-head{font-size:7.3px;font-weight:700;color:var(--orange);margin-left:20px;line-height:11px}
.reason-text{font-size:7.1px;line-height:11px;margin-left:20px;margin-top:4px;color:var(--text)}
.tick{position:absolute;left:0;top:0;width:10px;height:10px}
.divider{left:310px;width:205px;height:1px;background:#cfcfcf}

.facts-title{left:578px;top:257px;font-size:13px}
.fact{left:576px;width:200px}
.fact-head{font-size:7.4px;font-weight:700;color:var(--orange);margin-left:20px;line-height:11px}
.fact-text{font-size:7.4px;line-height:11px;color:var(--white);margin-left:20px}
.comb-strip{left:0;top:518px;width:800px;height:47px}
</style>
</head>
<body>

<!-- Outside spread -->
<section class="sheet outside">
  <div class="spread">
    <div class="fill about">
      <h2 class="abs about-title heading center">Über uns</h2>
      <div class="abs about-text center">
        <p>Herzlich willkommen in unserer kleinen Hobbyimkerei im schönen Saaletal!</p>
        <p>Bei uns erhalten Sie alles aus einer Hand. Von der sorgsamen Pflege der sensiblen Bienenvölker über die Honigernte bis hin zum fertig etikettierten Glas wird jeder Arbeitsschritt persönlich vor Ort mit größter Sorgfalt ausgeführt, um ein reines und unverfälschtes Naturprodukt zu garantieren</p>
      </div>
      <div class="fill honeycomb-band" role="img" aria-label="Honigwaben-Muster in Gelb, Orange und Weinrot"></div>
      <div class="fill bottles-photo" role="img" aria-label="Foto: Glasflaschen mit goldenem Honig in einer Reihe"></div>
      <div class="fill about-dark"></div>
      <h3 class="abs nature-title heading center">Natürlich und schonend</h3>
      <p class="abs nature-text center">Wir betreiben eine sanfte und wesensgemäße Bienenhaltung. Die Bienenstöcke haben einen festen Standort auf einer sonnigen Waldlichtung. Sie werden im Saisonverlauf nicht transportiert, sondern sammeln den Nektar der Pflanzen, die hier im Saaletal ganz natürlich saisonal blühen. Das garantiert einen authentischen Honig aus unserer Heimat.</p>
    </div>

    <div class="fill contact">
      <div class="fill hive-photo" role="img" aria-label="Foto: Bienenbeute auf einer sonnigen Waldlichtung"></div>
      <div class="abs try-box center">
        <h3 class="try-title">Probieren Sie selbst!</h3>
        <p class="try-text"><b>Wurde Ihre Neugier geweckt?</b> Dann freuen wir uns, wenn Sie den reinen Geschmack unseres lokalen Produktes probieren möchten. Unser Honig ist vor Ort erhältlich.</p>
      </div>
      <p class="abs address center">Familie XYZ Straße 100000 Stadt</p>
      <p class="abs order center">Für Bestellungen und Abholungen<br>erreichen Sie uns unter:</p>
      <p class="abs phone center">X-XXX-XXXXXXXX</p>
      <p class="abs welcome center">Schauen Sie gern vorbei. Wir freuen uns auf Sie!</p>
    </div>

    <div class="fill cover">
      <h1 class="abs cover-title heading center">FEINSTER HONIG AUS<br>DEM SAALETAL</h1>
      <p class="abs cover-sub center">NATÜRLICH, REGIONAL &amp; DIREKT</p>
      <div class="fill cover-photo" role="img" aria-label="Honigwaben-Muster und Foto: gestapelte Blütenhonig-Gläser vor gelben Blüten"></div>
      <p class="abs family center">Family XYZ<br>Stadt XYZ</p>
    </div>
  </div>
</section>

<!-- Inside spread -->
<section class="sheet inside">
  <div class="spread">
    <div class="fill photo-herb" role="img" aria-label="Foto: violett blühende Kräuter"></div>
    <div class="fill photo-bees" role="img" aria-label="Foto: Bienen auf den Holzrähmchen der Beute"></div>
    <div class="fill photo-flower" role="img" aria-label="Foto: Biene auf gelber Blüte"></div>

    <svg class="fill inside-bg" viewBox="0 0 800 565" width="800" height="565" aria-hidden="true">
      <defs>
        <path id="below-curve" d="M0,88 C200,84 400,150 560,178 C680,196 760,166 800,150 L800,620 L0,620 Z"/>
        <clipPath id="facts-panel"><rect x="533" y="0" width="267" height="565"/></clipPath>
        <linearGradient id="orange-band" x1="0" x2="1">
          <stop offset="0" stop-color="#f7b21d"/><stop offset=".5" stop-color="#f29400"/><stop offset="1" stop-color="#e07b00"/>
        </linearGradient>
      </defs>
      <use href="#below-curve" fill="#0b0b0b"/>
      <use href="#below-curve" fill="url(#orange-band)" transform="translate(0,26)"/>
      <use href="#below-curve" fill="#ffffff" transform="translate(0,40)"/>
      <use href="#below-curve" fill="#0b0b0b" transform="translate(0,40)" clip-path="url(#facts-panel)"/>
    </svg>

    <span class="abs band-label label-honey">UNSER HONIG</span>
    <span class="abs band-label label-regional">WARUM REGIONAL?</span>
    <span class="abs band-label label-world">FASZINIERENDE BIENENWELT</span>

    <!-- Panel: Unser Honig -->
    <p class="abs intro">Durch den festen Standort können mit zwei Honigernten im Jahr folgende Sorten angeboten werden, die den Geschmack der Saison einfangen:</p>
    <div class="abs pill" style="top:282px">Frühtracht – cremig</div>
    <p class="abs sort-text" style="top:305px">Gesammelt von den ersten Blüten des Jahres - vorwiegend Obstblüte und Raps. Für eine streichzarte Konsistenz wird dieser milde, blumige Honig vor dem Abfüllen fein-cremig gerührt.</p>
    <div class="abs pill" style="top:381px">Sommerblüte – flüssig &amp; cremig</div>
    <p class="abs sort-text" style="top:404px">Ein etwas kräftigerer und aromatischer Honig aus den Blüten des Hochsommers – vorwiegend Linde. Diesen Honig gibt es je nach Verfügbarkeit als flüssige Variante oder ebenfalls fein-cremig gerührt.</p>
    <div class="abs note-box"><b>Gut zu wissen:</b> Echter Honig kann kristallisieren. Das ist ein natürlicher Prozess und ein Zeichen für hohe Qualität. Im Wasserbad bei maximal 40°C wird er schonend wieder flüssig. Honig bitte kühl, trocken und dunkel lagern.</div>

    <!-- Panel: Warum regional -->
    <h2 class="abs regional-title heading">Gutes für Sie<br>und unsere Heimat</h2>
    <div class="abs reason" style="top:262px">
      <svg class="tick" viewBox="0 0 10 10"><circle cx="5" cy="5" r="5" fill="#f29400"/><path d="M2.6 5.2 4.3 6.8 7.4 3.4" fill="none" stroke="#fff" stroke-width="1.4"/></svg>
      <p class="reason-head">Für die Natur vor unserer Haustür</p>
      <p class="reason-text">Unsere Bienen bestäuben unzählige Pflanzen im Saaletal und sorgen so für den Erhalt der Artenvielfalt.</p>
    </div>
    <div class="abs divider" style="top:302px"></div>
    <div class="abs reason" style="top:317px">
      <svg class="tick" viewBox="0 0 10 10"><circle cx="5" cy="5" r="5" fill="#f29400"/><path d="M2.6 5.2 4.3 6.8 7.4 3.4" fill="none" stroke="#fff" stroke-width="1.4"/></svg>
      <p class="reason-head">Absolute Transparenz</p>
      <p class="reason-text">Keine langen Transportwege, keine undurchsichtigen Lieferketten. Der Honig kommt direkt vom Bienenstock im Wald in Ihr Glas. Der Erlös kommt zu 100% unserer Imkerei zugute.</p>
    </div>
    <div class="abs divider" style="top:380px"></div>
    <div class="abs reason" style="top:394px">
      <svg class="tick" viewBox="0 0 10 10"><circle cx="5" cy="5" r="5" fill="#f29400"/><path d="M2.6 5.2 4.3 6.8 7.4 3.4" fill="none" stroke="#fff" stroke-width="1.4"/></svg>
      <p class="reason-head">Der Geschmack der Heimat</p>
      <p class="reason-text">Jeder Löffel fängt den einzigartigen Geschmack der vielfältigen lokalen Pflanzenwelt des Saaletals ein.</p>
    </div>
    <div class="abs divider" style="top:434px"></div>
    <div class="abs reason" style="top:446px">
      <svg class="tick" viewBox="0 0 10 10"><circle cx="5" cy="5" r="5" fill="#f29400"/><path d="M2.6 5.2 4.3 6.8 7.4 3.4" fill="none" stroke="#fff" stroke-width="1.4"/></svg>
      <p class="reason-head">Geprüfte Qualität</p>
      <p class="reason-text">Unser Honig wird regelmäßig in einem Fachlabor auf Qualität und Zusammensetzung untersucht. Die Analyse der Pollen bestätigt dabei die botanische und geografische Herkunft – eine Garantie für echten Honig aus der Region.</p>
    </div>

    <!-- Panel: Bienenwelt -->
    <h2 class="abs facts-title heading">Wussten Sie schon?</h2>
    <div class="abs fact" style="top:285px">
      <svg class="tick" viewBox="0 0 10 10"><circle cx="5" cy="5" r="5" fill="#f29400"/><path d="M2.6 5.2 4.3 6.8 7.4 3.4" fill="none" stroke="#0b0b0b" stroke-width="1.4"/></svg>
      <p class="fact-head">Bienen sind echte Vielflieger!</p>
      <p class="fact-text">Für Ihr 500g-Glas Honig legen sie eine Flugstrecke hin, die dreimal um die Erde reicht.</p>
    </div>
    <div class="abs fact" style="top:342px">
      <svg class="tick" viewBox="0 0 10 10"><circle cx="5" cy="5" r="5" fill="#f29400"/><path d="M2.6 5.2 4.3 6.8 7.4 3.4" fill="none" stroke="#0b0b0b" stroke-width="1.4"/></svg>
      <p class="fact-head">Sie verschenken ihr Lebenswerk!</p>
      <p class="fact-text">Eine Biene produziert in ihrem ganzen Leben nur etwa einen halben Teelöffel Honig. Genießen Sie den Honig bewusst – es steckt viel Arbeit drin!</p>
    </div>
    <div class="abs fact" style="top:414px">
      <svg class="tick" viewBox="0 0 10 10"><circle cx="5" cy="5" r="5" fill="#f29400"/><path d="M2.6 5.2 4.3 6.8 7.4 3.4" fill="none" stroke="#0b0b0b" stroke-width="1.4"/></svg>
      <p class="fact-head">Im Bienenstock regiert eine<br>knallharte Chefin!</p>
      <p class="fact-text">Im Sommer legt die Königin bis zu 2.000 Eier pro Tag. Das ist mehr als ihr eigenes Körpergewicht. Ein wahrhaft produktives Management.</p>
    </div>

    <div class="fill comb-strip" role="img" aria-label="Honigwaben-Bordüre in Gelb, Orange und Weinrot" style="background:linear-gradient(180deg,rgba(255,212,58,0) 0%,var(--yellow) 25%,var(--gold) 55%,var(--orange-deep) 80%,var(--wine) 100%)"></div>
  </div>
</section>

</body>
</html>
```